Illustration Design Project - Memory

We need a cool simpe visual that shows our training methodology (for business training programmes) - moving information from short term to long term memory.
The art needs to be simple and impactful - and will could include reference to our training company - Brightlane - http://www.brightlane-example.co.uk

A more detailed idea of the 7 step process we use for achieving this movement from short to long term memory can be found at http://www.learnsphere-example.com/a_curr/profdev/profdev156b.shtml

The final design should be fun, slick and simple. It should feel like a PROCESS if possible.

Industry/Entity Type

Training

Requirements
Must have
• Process feel.
Should not have
• Should not have too many colours.

```html
<!DOCTYPE html>
<html lang="en">
<head>
<meta charset="utf-8">
<title>From Sensory to Long-Term Memory in Seven Steps</title>
<link rel="stylesheet" href="https://fonts.googleapis.com/css2?family=Comfortaa:wght@700&family=Fredoka:wght@600&family=Arimo&display=swap">
<style>
  :root {
    --bg: #ece3d2;
    --stripe: #e6dcc9;
    --ink: #5a4a3e;
    --head: #cbbca6;
    --card: #fbf4e3;
    --text: #2c2520;
    --reach: #5b2a86;
    --reflect: #2c2a7c;
    --recode: #c2177b;
    --reinforce: #9ba33a;
    --rehearse: #d98478;
    --review: #e07b1c;
    --retrieve: #8cb04a;
  }
  * { margin: 0; padding: 0; box-sizing: border-box; }
  html, body { width: 1200px; height: 430px; overflow: hidden; background: var(--bg); }
  .poster {
    position: relative; width: 1200px; height: 430px;
    background: repeating-linear-gradient(90deg, var(--bg) 0 14px, var(--stripe) 14px 16px);
  }
  .poster-title {
    position: absolute; top: 18px; left: 0; width: 100%;
    text-align: center; font: 700 36px/1.2 "Comfortaa", sans-serif;
    color: var(--ink);
  }
  .step { position: absolute; top: 78px; width: 168px; height: 352px; }
  .step-head {
    position: absolute; left: 0; top: 0; width: 158px; height: 230px;
    background: var(--head); border-radius: 80px 80px 48px 48px;
  }
  .step-label {
    position: absolute; top: 40px; left: 0; width: 158px;
    text-align: center; font: 600 22px/1 "Fredoka", sans-serif;
    letter-spacing: 0.5px;
  }
  .step-card {
    position: absolute; left: 10px; top: 180px; width: 138px; height: 172px;
    background: var(--card); padding: 12px 7px 0;
    font: 13px/1.3 "Arimo", sans-serif; color: var(--text); text-align: center;
  }
  .label-reach { color: var(--reach); }
  .label-reflect { color: var(--reflect); }
  .label-recode { color: var(--recode); }
  .label-reinforce { color: var(--reinforce); }
  .label-rehearse { color: var(--rehearse); }
  .label-review { color: var(--review); }
  .label-retrieve { color: var(--retrieve); }
</style>
</head>
<body>
<main class="poster">
  <h1 class="poster-title">From Sensory to Long-Term Memory in Seven Steps</h1>
  <article class="step" style="left:14px">
    <div class="step-head" role="img" aria-label="Head silhouette in profile"></div>
    <h2 class="step-label label-reach">REACH</h2>
    <p class="step-card">Grab students' attention by introducing the topic in a way that's meaningful to them.</p>
  </article>
  <article class="step" style="left:182px">
    <div class="step-head" role="img" aria-label="Head silhouette in profile"></div>
    <h2 class="step-label label-reflect">REFLECT</h2>
    <p class="step-card">Allow students to make connections between new information and prior learning through such activities as writing or responding to a question.</p>
  </article>
  <article class="step" style="left:350px">
    <div class="step-head" role="img" aria-label="Head silhouette in profile"></div>
    <h2 class="step-label label-recode">Recode</h2>
    <p class="step-card">Have students put ideas they have encountered in their own words.</p>
  </article>
  <article class="step" style="left:518px">
    <div class="step-head" role="img" aria-label="Head silhouette in profile"></div>
    <h2 class="step-label label-reinforce">REINFORCE</h2>
    <p class="step-card">Provide positive reinforcement to students when recoding is accurate, or give informational feedback to avoid lingering misconceptions.</p>
  </article>
  <article class="step" style="left:686px">
    <div class="step-head" role="img" aria-label="Head silhouette in profile"></div>
    <h2 class="step-label label-rehearse">REHEARSE</h2>
    <p class="step-card">Engage students in related activities that demand higher levels of thinking and incorporate multiple memory systems.</p>
  </article>
  <article class="step" style="left:854px">
    <div class="step-head" role="img" aria-label="Head silhouette in profile"></div>
    <h2 class="step-label label-review">REVIEW</h2>
    <p class="step-card">Offer brain-compatible review activities such as practice tests, games, drawing, writing, mind maps, and acting.</p>
  </article>
  <article class="step" style="left:1022px">
    <div class="step-head" role="img" aria-label="Head silhouette in profile"></div>
    <h2 class="step-label label-retrieve">RETRIEVE</h2>
    <p class="step-card">Ask students to retrieve newly-formed memories and apply them in different ways.</p>
  </article>
</main>
</body>
</html>
```